Brochure Design - Non-Profit Fundraising Stream

We are a non-profit organization that is developing a fundraising project through the donation of life insurance policies. We have three brochures in each English and French that we developed for a sister organization that we want to reintegrate with our Foundation, keeping the same copy text just changing the logos, colors and make it overall more visually appealing. The foundation is called the 'Varnek-Holt Syndrome Foundation Canada'.
The original files in .docx format are attached as is the full logo and two symbol files. The deliverables would be six documents in total (InDesign or .docx), each brochure in English and French. The color hex codes are:
red: #7b2850
dark blue: #2c79a7
pale blue: #78b2e2

```html
<!DOCTYPE html>
<html lang="en">
<head>
<meta charset="utf-8">
<title>Varnek-Holt Syndrome Foundation Canada — Life Insurance Donation Brochure</title>
<link href="https://fonts.googleapis.com/css2?family=Open+Sans:ital,wght@0,400;0,600;0,700;0,800;1,400;1,600;1,700&family=Roboto+Condensed:ital,wght@0,700;0,800;1,700&display=swap" rel="stylesheet">
<style>
  :root{
    --berry:#7b2850;
    --blue:#2c79a7;
    --pale:#78b2e2;
    --ink:#2a2a2a;
    --grey-row:#e4e6e9;
    --grey-line:#b9bec4;
    --stage:#efefef;
    --paper:#ffffff;
  }
  *{box-sizing:border-box;margin:0;padding:0}
  html,body{width:1200px;height:2705px;overflow:hidden}
  body{background:var(--stage);font-family:"Open Sans",Arial,sans-serif;color:var(--ink);position:relative}

  .page{position:absolute;width:550px;height:712px;background:var(--paper);overflow:hidden}
  .sheet{position:absolute;left:50px;width:1100px;height:712px;box-shadow:0 8px 24px rgba(0,0,0,.18)}
  .sheet .page{top:0}
  .sheet .page.left{left:0}
  .sheet .page.right{left:550px}
  .sheet::after{content:"";position:absolute;left:549px;top:0;width:2px;height:100%;background:rgba(0,0,0,.06)}
  .cover-solo{left:325px;top:70px;box-shadow:0 8px 24px rgba(0,0,0,.18)}
  .outside{top:960px}
  .inside{top:1830px}

  .art{position:absolute;inset:0}

  /* cover */
  .brand{position:absolute;display:flex;align-items:center;gap:10px;color:#fff;font-weight:700;font-size:17px;letter-spacing:.2px}
  .brand-dot{width:16px;height:16px;border-radius:50%;background:var(--pale);flex:none}
  .cover-brand{left:150px;top:500px}
  .headline{position:absolute;left:56px;top:535px;width:470px;font-family:"Roboto Condensed","Arial Narrow",sans-serif;font-weight:800;font-size:34px;line-height:1.02;color:#fff;text-transform:uppercase;text-align:center;letter-spacing:.3px}
  .cover-url{position:absolute;left:0;right:0;top:628px;text-align:center;color:#fff;font-weight:700;font-size:17px;letter-spacing:.3px}

  /* back page */
  .tab{position:absolute;background:var(--pale);color:#fff;font-weight:700;font-style:italic;text-transform:uppercase;font-size:13px;padding:4px 16px;letter-spacing:.5px}
  .process-tab{left:180px;top:48px}
  .process{position:absolute;left:24px;top:100px;width:500px;display:flex;justify-content:space-between}
  .step{width:92px;height:92px;border-radius:50%;border:4px solid var(--berry);border-right-color:var(--pale);display:flex;align-items:center;justify-content:center;text-align:center;font-size:8.5px;line-height:1.15;font-weight:700;font-style:italic;color:var(--blue);padding:10px;background:#fff}
  .step:nth-child(even){margin-top:26px;border-color:var(--pale);border-top-color:var(--berry)}

  .contact{position:absolute;left:60px;top:395px;display:flex;gap:18px;align-items:center}
  .contact-mark{width:42px;height:42px;border-radius:50%;background:var(--blue);flex:none}
  .contact-lines{font-style:italic;font-weight:700;font-size:17px;line-height:1.35;color:var(--ink)}
  .contact-lines .phone{display:flex;align-items:center;gap:7px}

  .disclosures{position:absolute;left:40px;top:500px;width:470px;border:2px solid var(--pale);border-radius:16px;padding:22px 22px 16px}
  .disclosures h3{position:absolute;top:-11px;left:50%;transform:translateX(-50%);background:#fff;padding:0 10px;color:var(--blue);font-style:italic;font-weight:800;font-size:13px;text-transform:uppercase}
  .disclosures ul{list-style:none}
  .disclosures li{position:relative;padding-left:14px;font-size:9px;font-style:italic;font-weight:600;line-height:1.35;margin-bottom:5px}
  .disclosures li::before,.bullets li::before{content:"";position:absolute;left:0;top:4px;width:6px;height:6px;border-radius:50%;background:var(--berry)}

  /* inside left */
  .photo-slot{position:absolute;left:0;top:0;width:300px;height:300px;background:linear-gradient(160deg,#f3e6b4 0%,#c9b46a 35%,#7a7c4c 65%,#6b6b62 100%)}
  .intro{position:absolute;left:300px;top:0;width:250px;height:300px;background:var(--pale);color:#fff;font-style:italic;font-weight:600;font-size:11.6px;line-height:1.42;padding:22px 20px;text-align:justify}
  .adv-title{position:absolute;left:30px;top:318px;color:var(--blue);font-family:"Roboto Condensed","Arial Narrow",sans-serif;font-style:italic;font-weight:700;font-size:19.5px;text-transform:uppercase;letter-spacing:.2px}
  .bullets{position:absolute;list-style:none}
  .bullets li{position:relative;padding-left:14px;font-size:11px;line-height:1.3;margin-bottom:10px}
  .bullets small{font-size:9px}
  .adv-a{left:30px;top:358px;width:240px}
  .adv-b{left:290px;top:358px;width:230px}
  .suit-tab{left:0;top:480px;font-size:16px;padding:6px 30px 6px 40px;font-style:normal;font-weight:600}
  .suit-a{left:30px;top:525px;width:240px}
  .suit-b{left:290px;top:525px;width:230px}
  .slogan{position:absolute;left:30px;top:595px;font-family:"Roboto Condensed","Arial Narrow",sans-serif;font-weight:800;font-size:28px;text-transform:uppercase;color:#111;letter-spacing:.2px}
  .foot{position:absolute;left:30px;right:30px;top:650px;display:flex;align-items:center;gap:12px}
  .foot-brand{display:flex;align-items:center;gap:6px;color:var(--blue);font-weight:700;font-size:10px;width:170px;line-height:1.2}
  .foot-brand .brand-dot{width:12px;height:12px}
  .foot-rule{flex:1;height:2px;background:var(--blue)}
  .foot-url{color:var(--blue);font-weight:700;font-size:13px}

  /* inside right: FAQ */
  .faq{position:absolute;left:22px;top:28px;width:506px;border-collapse:separate;border-spacing:3px 0;font-size:8.2px;line-height:1.25}
  .faq th{background:var(--blue);color:#fff;font-weight:700;font-size:12px;padding:5px;text-transform:uppercase;border-radius:8px 8px 0 0}
  .faq td{vertical-align:top;padding:4px 6px;border-bottom:1px solid var(--grey-line)}
  .faq td.q{width:46%;font-weight:700;background:var(--grey-row)}
  .faq td.a{background:#f5f6f7}
  .faq td.q.mid{vertical-align:middle}
  .faq ul{list-style:none;margin-top:2px}
  .faq li{position:relative;padding-left:9px}
  .faq li::before{content:"";position:absolute;left:0;top:3px;width:4px;height:4px;border-radius:50%;background:var(--berry)}
  .faq li li{margin-left:9px}
  .faq strong{font-weight:800}
</style>
</head>
<body>

<!-- Front cover -->
<section class="page cover-solo" aria-label="Brochure front cover">
  <svg class="art" viewBox="0 0 550 712" aria-hidden="false">
    <defs>
      <linearGradient id="photoTone1" x1="0" y1="0" x2="0" y2="1">
        <stop offset="0" stop-color="#e9e8ee"/><stop offset=".45" stop-color="#d9b9a6"/><stop offset=".7" stop-color="#c9877a"/><stop offset="1" stop-color="#d7d4dc"/>
      </linearGradient>
      <radialGradient id="bandGlow1" cx=".62" cy=".3" r=".6">
        <stop offset="0" stop-color="#f4f8fc"/><stop offset=".35" stop-color="#a9cdea"/><stop offset="1" stop-color="#2c79a7"/>
      </radialGradient>
    </defs>
    <path role="img" aria-label="Photo: cupped hands holding a red felt heart" fill="url(#photoTone1)" d="M0 0H550V210C470 360 300 450 0 470Z"/>
    <path fill="url(#bandGlow1)" d="M0 486C300 470 480 380 550 240V650C400 690 200 705 0 690Z"/>
    <path fill="none" stroke="#7b2850" stroke-width="6" d="M0 478C300 462 480 372 550 232"/>
    <path fill="#fff" d="M0 712V690C220 708 420 690 550 650V712Z"/>
    <path fill="none" stroke="#2c79a7" stroke-width="3" d="M150 690C320 695 460 670 550 630"/>
  </svg>
  <div class="brand cover-brand"><span class="brand-dot"></span>Varnek-Holt Syndrome Foundation Canada</div>
  <h1 class="headline">Unlock the hidden value<br>in your life insurance</h1>
  <p class="cover-url">www.varnekholtcanada.org</p>
</section>

<!-- Outside spread -->
<div class="sheet outside" aria-label="Brochure outside spread">
  <section class="page left" aria-label="Back cover">
    <svg class="art" viewBox="0 0 550 712" aria-hidden="true">
      <path fill="#2c79a7" d="M0 300C130 240 330 250 550 340V470C380 360 180 330 0 370Z"/>
      <path fill="none" stroke="#7b2850" stroke-width="6" d="M40 268C170 225 360 245 550 325"/>
    </svg>
    <div class="tab process-tab">Donation Process</div>
    <div class="process">
      <div class="step">Complete Application Form &amp; Provide Policy Documents and Illustrations</div>
      <div class="step">Provide Medical Information</div>
      <div class="step">Determine Amount of Tax Receipt</div>
      <div class="step">Sign Ownership Transfer Documents</div>
      <div class="step">Convert the Tax Receipt into $$$ in your Pocket</div>
    </div>
    <div class="contact">
      <span class="contact-mark"></span>
      <div class="contact-lines">
        <div class="phone">
          <svg width="14" height="14" viewBox="0 0 24 24" aria-hidden="true"><path fill="#2c79a7" d="M6.6 10.8a15 15 0 006.6 6.6l2.2-2.2a1 1 0 011-.25 11.4 11.4 0 003.6.57 1 1 0 011 1V20a1 1 0 01-1 1A17 17 0 013 4a1 1 0 011-1h3.5a1 1 0 011 1c0 1.25.2 2.45.57 3.6a1 1 0 01-.25 1Z"/></svg>
          1(800) 555-0147
        </div>
        <div>info@varnekholtcanada.org</div>
        <div>varnekholtcanada.org</div>
      </div>
    </div>
    <div class="disclosures">
      <h3>Disclosures</h3>
      <ul>
        <li>Proceeds are treated as a disposition for tax purposes and are taxed on excess amount over adjusted cost basis, which includes all premiums paid on the policy less the net cost of pure insurance. Policy holders should seek their own independent professional tax, legal and financial advice.</li>
        <li>A change of ownership of a policy may in the future limit the insured's ability to purchase additional insurance as a result of limits on how much coverage insurers will issue.</li>
        <li>Donors of life insurance policies will be required to provide consent to allow access to medical records for purposes of evaluating the life insurance policy. This information will be maintained on a confidential basis.</li>
      </ul>
    </div>
  </section>

  <section class="page right" aria-label="Front cover">
    <svg class="art" viewBox="0 0 550 712">
      <defs>
        <linearGradient id="photoTone2" x1="0" y1="0" x2="0" y2="1">
          <stop offset="0" stop-color="#e9e8ee"/><stop offset=".45" stop-color="#d9b9a6"/><stop offset=".7" stop-color="#c9877a"/><stop offset="1" stop-color="#d7d4dc"/>
        </linearGradient>
        <radialGradient id="bandGlow2" cx=".62" cy=".3" r=".6">
          <stop offset="0" stop-color="#f4f8fc"/><stop offset=".35" stop-color="#a9cdea"/><stop offset="1" stop-color="#2c79a7"/>
        </radialGradient>
      </defs>
      <path role="img" aria-label="Photo: cupped hands holding a red felt heart" fill="url(#photoTone2)" d="M0 0H550V210C470 360 300 450 0 470Z"/>
      <path fill="url(#bandGlow2)" d="M0 486C300 470 480 380 550 240V650C400 690 200 705 0 690Z"/>
      <path fill="none" stroke="#7b2850" stroke-width="6" d="M0 478C300 462 480 372 550 232"/>
      <path fill="#fff" d="M0 712V690C220 708 420 690 550 650V712Z"/>
      <path fill="none" stroke="#2c79a7" stroke-width="3" d="M150 690C320 695 460 670 550 630"/>
    </svg>
    <div class="brand cover-brand"><span class="brand-dot"></span>Varnek-Holt Syndrome Foundation Canada</div>
    <h2 class="headline">Unlock the hidden value<br>in your life insurance</h2>
    <p class="cover-url">www.varnekholtcanada.org</p>
  </section>
</div>

<!-- Inside spread -->
<div class="sheet inside" aria-label="Brochure inside spread">
  <section class="page left" aria-label="Advantages page">
    <div class="photo-slot" role="img" aria-label="Photo: young plant growing from a glass jar of coins"></div>
    <p class="intro">You can maintain or substantially improve your financial position by unlocking the hidden value of your unwanted or unaffordable life insurance via a charitable donation. Every year, seniors over the age of 70 lapse or surrender almost $7 billion of insurance that they might otherwise donate to a charity. You can pay down debt, make major purchases or replenish retirement savings by accessing the value you deserve after paying premiums for decades.</p>
    <h2 class="adv-title">Advantages of donating a life insurance policy</h2>
    <ul class="bullets adv-a">
      <li>You obtain a tax receipt <small>(good for 5 years)</small> for 10%-50% of the face value of the policy <small>(even for term policies that have no "cash surrender value")</small></li>
      <li>You convert a "worthless or low cash value policy" into cash in your pocket when you file your income taxes</li>
    </ul>
    <ul class="bullets adv-b">
      <li>Eliminate the burden of annual premium expenses</li>
      <li>A Foundation becomes the owner and beneficiary, and it funds the premiums and collects the benefit upon maturity</li>
    </ul>
    <div class="tab suit-tab">Suitable policies</div>
    <ul class="bullets suit-a">
      <li>Term, Whole life, Universal or term-to-100 policies</li>
      <li>Insured lives over 70 years old</li>
    </ul>
    <ul class="bullets suit-b">
      <li>In-force greater than 2 years</li>
      <li>Minimum death benefit of $50,000</li>
    </ul>
    <p class="slogan">Maintain financial independence</p>
    <div class="foot">
      <div class="foot-brand"><span class="brand-dot"></span>Varnek-Holt Syndrome Foundation Canada</div>
      <span class="foot-rule"></span>
      <span class="foot-url">www.varnekholtcanada.org</span>
    </div>
  </section>

  <section class="page right" aria-label="Questions and answers page">
    <table class="faq" lang="fr">
      <thead><tr><th>Questions</th><th>Réponses</th></tr></thead>
      <tbody>
        <tr><td class="q">Quels sont les types de polices admissibles?</td><td class="a">Les polices temporaires et les polices permanentes (vie entière et universelles)</td></tr>
        <tr><td class="q">Qui prend en charge la souscription médicale?</td><td class="a">La Fondation</td></tr>
        <tr><td class="q">Qui prend en charge la souscription actuarielle?</td><td class="a">La Fondation</td></tr>
        <tr><td class="q">Quels montants d'assurance acceptez-vous?</td><td class="a">Entre 50 000 $ et 10 M $</td></tr>
        <tr><td class="q mid">Quels sont vos critères de sélection?</td><td class="a">À la base, l'espérance de vie (EV) de l'assuré ne doit pas dépasser cinq ans. Toutefois, dans certains cas, un assuré peut être admissible même s'il a une espérance de vie supérieure à cinq ans. Voici notre règle empirique : l'assuré a au moins 70 ans et il a des problèmes de santé ou il a au moins 80 ans et il est en bonne santé.</td></tr>
        <tr><td class="q">Qui assume le paiement des primes après le don de la police?</td><td class="a">La Fondation</td></tr>
        <tr><td class="q">Qui est propriétaire de la police après qu'elle a été offerte en don?</td><td class="a">La Fondation</td></tr>
        <tr><td class="q">Qui prend en charge les procédures relatives au contrôle préalable et aux souscriptions?</td><td class="a">La Fondation</td></tr>
        <tr><td class="q mid">Comment le processus se déroule-t-il?</td><td class="a">Vous communiquez avec nous par téléphone ou par courriel, en nous fournissant les renseignements suivants :
          <ul>
            <li>La valeur nominale de la police</li>
            <li>Le montant de la prime annuelle (montant actuel et montant au moment du renouvellement)</li>
            <li>Le type de police dont il s'agit
              <ul><li>S'il s'agit d'une assurance temporaire, est-elle convertible sans souscription médicale?</li></ul></li>
            <li>La date d'expiration de la police</li>
            <li>Les problèmes de santé de l'assuré</li>
            <li>L'âge de l'assuré</li>
          </ul></td></tr>
        <tr><td class="q">Depuis combien de temps la police doit-elle être en vigueur?</td><td class="a">La police doit être en vigueur depuis plus de deux ans.</td></tr>
        <tr><td class="q mid">Sur combien de temps le processus s'échelonne-t-il?</td><td class="a">Triage : moins d'une semaine<br>Souscription médicale : 1 à 2 semaines<br>Souscription actuarielle : 1 semaine<br>Formalités relatives au don : 1 jour<br><strong>Durée totale : 3 à 4 semaines</strong></td></tr>
        <tr><td class="q">Quel est généralement le montant du reçu aux fins d'impôt qui est remis au donateur?</td><td class="a">Ce montant varie selon les prévisions de l'espérance de vie de l'assuré, qui reposent sur son âge et son état de santé.</td></tr>
        <tr><td class="q">Que se passe-t-il si l'un de mes proches parents souhaite devenir bénéficiaire de la police?</td><td class="a">Avant d'approuver le don d'une police, nous devons nous assurer qu'aucun proche parent ne souhaite se porter acquéreur de celle-ci.</td></tr>
        <tr><td class="q">Un tel don est-il légal?</td><td class="a">Oui, tout le processus est légal, éthique et approuvé par le gouvernement.</td></tr>
        <tr><td class="q mid">Mais qu'est-ce que j'y gagne?</td><td class="a">Vous aviez prévu annuler votre police afin de ne plus avoir à assumer le paiement des primes. La Fondation assume le paiement de celles-ci (vous faites donc une économie d'argent), et vous obtenez en retour un reçu aux fins de l'impôt qui vous permet d'en tirer un avantage pécuniaire.</td></tr>
      </tbody>
    </table>
  </section>
</div>

</body>
</html>
```